Tally Roster survey and prize

We need an A4 poster design for a survey and competition I wish to hold. The survey will be on Poll Parrot. My website www.TallyRoster.com.au will redirect the users to the survey page. I will be selecting a survey entrant at random to win a prize. The prize is $200 cash. The survey will be open for two months as the mail out of this poster will go throughout Victoria, Australia. The competition end date is yet to be decided - depends on when I can get this poster completed and the mail out done.

The mail out is targeting the Aged Care industry workers and decision makers. It hopefully will be placed on a notice board in the facilities and need to attract attention for people to visit my site and then take the survey.

The survey is for not for residents but for the workers in the facility.
Updates

Reason: Just got some feedback on required content of the poster. Text for the poster required: "The survey is for determining a market for rostering and payroll software, your assitance in taking this survey would be greatly appreciated." Martin Hobbs

Target Market(s)

Workers in Aged Care industry and decision makers.

Industry/Entity Type

Industry

Requirements
Must have
• 1. Must reference the website www.TallyRoster.com.au.
2. Must mention that there is a prize of $200.
3. Must mention that entry to the competition is dependant on taking the survey.
4. Must mention the close date (date yet to be decided).
5. Must mention winning contestant will be contacted by phone.

```html
<!DOCTYPE html>
<html lang="en">
<head>
<meta charset="utf-8">
<title>How's Work Going? – Tally Roster Staff Survey</title>
<link rel="stylesheet" href="https://fonts.googleapis.com/css2?family=Fira+Sans:ital,wght@0,400;0,700;0,800;1,400&display=swap">
<style>
  :root {
    --sky: #00aeef;
    --scene-deep: #1489c2;
    --scene-mid: #2f9bd3;
    --mascot: #3b8fd6;
    --white: #ffffff;
    --yellow: #fff200;
    --shadow-blue: #1796d6;
    --ink: #1c3a57;
  }
  * { margin: 0; padding: 0; box-sizing: border-box; }
  html, body { width: 898px; height: 1200px; overflow: hidden; background: var(--sky); }
  .poster {
    position: relative;
    width: 898px;
    height: 1200px;
    background: var(--sky);
    font-family: "Fira Sans", Arial, sans-serif;
    color: var(--white);
    overflow: hidden;
  }
  .headline { position: absolute; left: 0; right: 0; text-align: center; font-weight: 800; line-height: 1; white-space: nowrap; }
  .headline-top { top: 88px; font-size: 122px; letter-spacing: -1px; padding-left: 40px; }
  .headline-main { top: 212px; font-size: 222px; letter-spacing: -2px; padding-left: 40px; }
  .mascot {
    position: absolute;
    left: 614px; top: 60px;
    width: 64px; height: 52px;
    border-radius: 40% 40% 45% 45%;
    background: var(--mascot);
  }
  .scene {
    position: absolute;
    left: 80px; top: 474px;
    width: 798px; height: 414px;
  }
  .invite {
    position: absolute;
    top: 902px; left: 0; right: 0;
    text-align: center;
    font-size: 36px;
    font-weight: 700;
    color: #eef7fc;
    white-space: nowrap;
    padding-left: 30px;
  }
  .prize {
    position: absolute;
    top: 940px; left: 0; right: 0;
    text-align: center;
    font-size: 176px;
    font-weight: 800;
    line-height: 1;
    white-space: nowrap;
    text-shadow: -6px -3px 0 var(--shadow-blue);
    padding-left: 30px;
  }
  .prize-win { color: var(--yellow); margin-right: 22px; }
  .prize-amount { color: var(--white); }
  .terms {
    position: absolute;
    top: 1107px; left: 0; right: 0;
    text-align: center;
    font-size: 17.5px;
    line-height: 1.3;
    color: var(--ink);
    white-space: nowrap;
    padding-left: 40px;
  }
  .terms em { font-style: italic; }
</style>
</head>
<body>
<main class="poster">
  <h1>
    <span class="headline headline-top">HOW’S WORK</span>
    <span class="headline headline-main">GOING?</span>
  </h1>
  <div class="mascot" role="img" aria-label="Small blue cartoon bird mascot perched on the letter O"></div>

  <svg class="scene" viewBox="0 0 798 414" role="img" aria-label="Cartoon park scene with trees, a carer in green scrubs and an elderly resident using a walking frame">
    <defs>
      <linearGradient id="scene-fill" x1="0" y1="0" x2="0" y2="1">
        <stop offset="0" stop-color="#2f9bd3"/>
        <stop offset="1" stop-color="#1489c2"/>
      </linearGradient>
    </defs>
    <rect width="798" height="414" rx="24" fill="url(#scene-fill)"/>
  </svg>

  <p class="invite">Participate in the staff survey and be in to</p>
  <p class="prize"><span class="prize-win">WIN</span><span class="prize-amount">$200</span></p>
  <p class="terms">Please take the time to fill in this survey at <em>www.TallyRoster.com.au</em> to enter the draw<br>Hurry! survey closes on&nbsp; 00/00/2012 and the winner will be contacted by phone.</p>
</main>
</body>
</html>
```